THE WYVERN is a mystical scythian creature, which guarded a golden treasure.

i am a published author back in he 1970's...corvell, edwin talbot, pemberly vance. my agent died and the companies have been bought.
i want to publish on my own and have 3 completed novels. DAS MOOR is the first. i need a book cover, spine and back cover design for the book.
i will use the book design as an important part of a website i am planning for this and the other 2 books. i will need a design for the other books once this is completed.

this book is a thriller; the second is a historical novel, the third is a comedy. i don't know, because of the differing contents whether there should be an consistency in the design. i think not.

i have an excellent Vellmar review and will want phrases from it prominently on the design. i like to be involved in the process. although the thriller deals with the Nazis, i don't want a bunch of s.s. officers. I see the book as a labyrinth with almost unbearable twists and turns. it is not a person book, but driven by the PLOT.

the design must be setup for PrintNook ( zentora ) for printing. Font is important.i like black, but not critical.

the Vellmar review (below) has an excellent outline and telling of the book.

as the other 2 novels are completed and i need help with a website, this could be more than just one project.

i would like a small photo and 2 line bio next to the photo.on back cover if it fits.... leaving room for the IBSN /barcode.
the cover, design and excerpts are critical for success and i am willing to work and pay extra to have it the best.
i have never done this before as my first 2 novels were published by traditional houses, so, you must forgive any awkwardness in the process.
thank you
+++++++

THIS IS THE VELLMAR REVIEW OF THE BOOK::::::::::
DAS MOOR (THE WYVERN)
Lindqvist, Tomas
Manuscript
BOOK REVIEW
Lindqvist (The Quiet Menders, 1983, etc.) offers an animated chase through Boston and Europe as his characters unravel
a mystery involving six pairs of identical Jewish twins saved from a German concentration camp.
In 1965, Oscar Dufresne, a scientist fruitlessly searching for the secret of telepathy, receives a tantalizing report of
macabre experiments conducted by Edgar Voskuil, a Nazi researcher on a similar mission. Dufresne searches for the
twins who were the subjects of Voskuil’s experiments, and he gets help from Ilse Marek, the daughter of another
German who was a pawn in a scheme to smuggle unknown items of the collapsing Reich. The first twin they
discover—Hedda Lintzer, a woman who had lived a solitary life in a Jewish neighborhood of Boston—is already dead,
the victim of a grisly murder. Her stomach had been sliced open and an odd, smaller tear made in the area of her
appendix. It soon turns out that, not long before her death, Lintzer discovered that she was a beneficiary of a mysterious
will. The search then jumps the Atlantic to England, where Calder, the powerful company funding Dufresne’s research,
pushes Welbury, the bank that served as an executor for the will, to release information on another set of twins—who also
turn out to be dead. The novel’s settings are vivid and refreshingly detailed and include a grotesque concentration camp
in Jena, Germany, as well as the Arcadian French Riviera. The cast of villains is equally colorful, and the story takes
many unexpected turns. Dufresne, on the other hand, is a stock protagonist about whom readers learn little more than his
hair color, his profession, and the fact that he enjoys sailing. Calder, meanwhile, has the convenient ability to coerce
any organization or suspect, but it’s never treated with any scrutiny itself. The novel could also have used a stronger
copy edit; for example, various characters’ thoughts are rendered inconsistently, either in all-caps or underlined. Despite
these issues, however, the overall story is excellent and a reason to look forward to more from this author.
An often audacious Nazi mystery with plenty of well-placed plot twists.

FOR ALL DESIGNERS!!!!!!!!!below is the story of DAS MOOR, ( THE WYVERN.)FOR THOSE DESIGNERS WHO COULD NOT OPEN THE FILE ON THE CONTEST PAGE.DAS MOOR (THE WYVERN)Hirschhorn, RichardManuscriptBOOK REVIEWHirshhorn (The Quiet Menders, 1983, etc.) offers an animated chase through Boston and Europe as his characters unravela mystery involving six pairs of identical Jewish twins saved from a German concentration camp.In 1965, Oscar Dufresne, a scientist fruitlessly searching for the secret of telepathy, receives a tantalizing report ofmacabre experiments conducted by Edgar Voskuil, a Nazi researcher on a similar mission. Dufresne searches for thetwins who were the subjects of Voskuil’s experiments, and he gets help from Ilse Marek, the daughter of anotherGerman who was a pawn in a scheme to smuggle unknown items of the collapsing Reich. The first twin theydiscover—Hedda Lintzer, a woman who had lived a solitary life in a Jewish neighborhood of Boston—is already dead,the victim of a grisly murder. Her stomach had been sliced open and an odd, smaller tear made in the area of herappendix. It soon turns out that, not long before her death, Lintzer discovered that she was a beneficiary of a mysteriouswill. The search then jumps the Atlantic to England, where Calder, the powerful company funding Dufresne’s research,pushes Welbury, the bank that served as an executor for the will, to release information on another set of twins—who alsoturn out to be dead. The novel’s settings are vivid and refreshingly detailed and include a grotesque concentration campin Jena, Germany, as well as the Arcadian French Riviera. The cast of villains is equally colorful, and the story takesmany unexpected turns. Dufresne, on the other hand, is a stock protagonist about whom readers learn little more than hishair color, his profession, and the fact that he enjoys sailing. Calder, meanwhile, has the convenient ability to coerceany organization or suspect, but it’s never treated with any scrutiny itself. The novel could also have used a strongercopy edit; for example, various characters’ thoughts are rendered inconsistently, either in all-caps or underlined. Despitethese issues, however, the overall story is excellent and a reason to look forward to more from this author.An often audacious Nazi mystery with plenty of well-placed plot twists. Added Tuesday, June 2, 2015

BUDGET NOW $700 !!!!!!! STORY DETAILS NOW UPLOADED TO THE BRIEF.

BUDGET OVER $700 !!!!!!!

adult; males; history buffs; world war II buffs; groups interested in mental telepathy;
people who want their money's worth ona challenging read; people who have faith in the Vellmar Reviews.

Sans Serif
• arial.

• front and back cover, spine. a design which grabs enough to want to read back text.
• design to emphasize the puzzle, labyrinth,, riddle, complexity, deceptions, twists, false leads,masquerades,double-dealing, trickiness of the plot.
• presence of identical twins; a treasure.
• the naivety of the american; the duplicities of the germans; the diabolical schemes of the germans. the vulnerability of the children. the ??? suspect mental capability of the identical twins.
• marching nazis,
• ? prominent swastika.
• no horror.
• no supernatural mumbo-jumbo.

```html
<!DOCTYPE html>
<html lang="en">
<head>
<meta charset="utf-8">
<title>The Wyvern – Spine and Front Cover</title>
<link rel="stylesheet" href="https://fonts.googleapis.com/css2?family=Cinzel:wght@400;700&family=Josefin+Sans:wght@400&display=swap">
<style>
  :root {
    --page: #ececec;
    --cover-black: #0b0a0a;
    --cover-maroon: #2a0d0b;
    --spine-black: #080707;
    --gold-light: #f4dc8a;
    --gold-mid: #c99a3c;
    --gold-dark: #7a5518;
    --subtitle-red: #6b2a1e;
    --author-white: #f2f0ec;
    --scene-ember: #c8621c;
    --scene-glow: #f1c27a;
    --scene-dark: #1a0807;
  }
  * { margin: 0; padding: 0; box-sizing: border-box; }
  html, body {
    width: 1200px;
    height: 1200px;
    overflow: hidden;
  }
  body {
    background: var(--page);
    position: relative;
  }
  .gold-text {
    font-family: "Cinzel", serif;
    font-weight: 700;
    background: linear-gradient(180deg, var(--gold-light) 0%, var(--gold-mid) 55%, var(--gold-dark) 100%);
    -webkit-background-clip: text;
    background-clip: text;
    color: transparent;
  }

  /* Spine */
  .spine {
    position: absolute;
    left: 282px;
    top: 100px;
    width: 95px;
    height: 1000px;
    background: var(--spine-black);
    overflow: hidden;
  }
  .spine-title {
    position: absolute;
    top: 110px;
    left: 0;
    width: 95px;
    height: 300px;
    writing-mode: vertical-rl;
    display: flex;
    align-items: center;
    justify-content: center;
    text-align: center;
    gap: 2px;
  }
  .spine-title-article {
    font-size: 20px;
    letter-spacing: 2px;
  }
  .spine-title-main {
    font-size: 56px;
    line-height: 1;
  }
  .spine-subtitle {
    font-family: "Josefin Sans", sans-serif;
    font-size: 14px;
    letter-spacing: 6px;
    color: var(--subtitle-red);
  }
  .spine-author {
    position: absolute;
    top: 550px;
    left: 0;
    width: 95px;
    height: 420px;
    writing-mode: vertical-rl;
    display: flex;
    align-items: center;
    justify-content: center;
    font-family: "Josefin Sans", sans-serif;
    font-size: 30px;
    letter-spacing: 2px;
    color: var(--author-white);
  }

  /* Front cover */
  .front-cover {
    position: absolute;
    left: 377px;
    top: 100px;
    width: 540px;
    height: 1000px;
    background:
      radial-gradient(ellipse at 50% 45%, var(--cover-maroon) 0%, var(--cover-black) 70%),
      var(--cover-black);
    overflow: hidden;
  }
  .title-block {
    position: absolute;
    top: 70px;
    left: 0;
    width: 100%;
    text-align: center;
  }
  .title-article {
    display: block;
    font-size: 44px;
    letter-spacing: 3px;
    line-height: 1;
  }
  .title-main {
    display: block;
    font-size: 104px;
    line-height: 1;
    margin-top: 4px;
  }
  .subtitle {
    font-family: "Josefin Sans", sans-serif;
    font-size: 26px;
    letter-spacing: 11px;
    padding-left: 11px;
    color: var(--subtitle-red);
    margin-top: 2px;
  }
  .cover-scene {
    position: absolute;
    top: 275px;
    left: 20px;
    width: 500px;
    height: 555px;
  }
  .author-name {
    position: absolute;
    top: 858px;
    left: 0;
    width: 100%;
    text-align: center;
    font-family: "Josefin Sans", sans-serif;
    font-size: 38px;
    letter-spacing: 1px;
    color: var(--author-white);
  }
</style>
</head>
<body>
  <aside class="spine">
    <div class="spine-title">
      <span class="spine-title-article gold-text">THE</span>
      <span class="spine-title-main gold-text">WYVERN</span>
      <span class="spine-subtitle">DAS MOOR</span>
    </div>
    <p class="spine-author">TOMAS LINDQVIST</p>
  </aside>

  <main class="front-cover">
    <header class="title-block">
      <span class="title-article gold-text">THE</span>
      <h1 class="title-main gold-text">WYVERN</h1>
      <p class="subtitle">DAS MOOR</p>
    </header>

    <svg class="cover-scene" viewBox="0 0 500 555" role="img"
         aria-label="Illustration: glowing round vault door in a brick wall between two clock towers, silhouettes of children behind barbed wire in a fiery haze">
      <defs>
        <radialGradient id="sceneGlow" cx="50%" cy="45%" r="62%">
          <stop offset="0%" stop-color="var(--scene-glow)"/>
          <stop offset="35%" stop-color="var(--scene-ember)"/>
          <stop offset="75%" stop-color="var(--scene-dark)"/>
          <stop offset="100%" stop-color="var(--cover-black)" stop-opacity="0"/>
        </radialGradient>
      </defs>
      <rect x="0" y="0" width="500" height="555" fill="url(#sceneGlow)"/>
    </svg>

    <p class="author-name">TOMAS LINDQVIST</p>
  </main>
</body>
</html>
```